Halvern Properties Business Cards

I would like a business card that includes myself and my partner.
Includes: Logo, office #, email, website, our names, our numbers and possibly the address. I would also like the logo to be embossed and the card to be horizontal.
There is a photo of our yard signs to give you an idea of the colors of our business.

Target Market(s)

Everyone in real estate market.
We are in a rural area. Our clientele are from all socioeconomic backgrounds.

Industry/Entity Type

Real Estate Agent

Contact Information for Business Card

Company Name: Halvern Properties
Our Names, Titles & Cell #'s : Marla Halvern-Broker (555).316.4827, Tessa Halvern-Realtor (555).627.9154
Office #: (555).841.2600
Website: halvernproperties-example.com
Joint Email: halvern@halvernproperties-example.com
Office Address: 518B W. Cottonwell Ave.
Ferrow Glen, ZX. 70999

Font styles to use
Serif

Requirements
Must have
• HORIZONTAL, Logo, Myself and my partners names, Our cell #'s, our office #, our website, our email address
Nice to have
• Embossed logo, office address, our titles.

```html
<!DOCTYPE html>
<html lang="en">
<head>
<meta charset="utf-8">
<title>Halvern Properties — Business Card</title>
<link rel="stylesheet" href="https://fonts.googleapis.com/css2?family=Cinzel:wght@400;600;700&display=swap">
<style>
  :root {
    --page-bg: #d9d9d9;
    --card-black: #050407;
    --glow-purple: #3b2560;
    --ink-white: #f4f2f6;
    --ink-soft: #d6d2dc;
    --ink-muted: #8d8893;
    --rule-purple: #5a4675;
    --emboss-white: #f1f0ef;
  }
  * { box-sizing: border-box; margin: 0; padding: 0; }
  html, body {
    width: 1200px; height: 800px; overflow: hidden;
    background: var(--page-bg);
    font-family: "Cinzel", Georgia, serif;
  }
  .card {
    position: absolute; left: 75px; top: 100px;
    width: 1050px; height: 600px;
    border-radius: 36px; overflow: hidden;
    background:
      radial-gradient(ellipse 420px 300px at 600px 300px, var(--glow-purple) 0%, rgba(40,22,66,0.6) 45%, rgba(5,4,7,0) 100%),
      var(--card-black);
    color: var(--ink-white);
  }
  .emboss-mark {
    position: absolute; left: -330px; top: 70px;
    width: 560px; height: 560px; border-radius: 50%;
    background: var(--emboss-white);
  }
  .brand {
    position: absolute; right: 60px; top: 52px;
    display: flex; align-items: center; gap: 18px;
  }
  .brand-dot {
    width: 62px; height: 62px; border-radius: 50%;
    background: var(--ink-white);
  }
  .brand-name {
    font-weight: 600; font-size: 44px; letter-spacing: 1px;
    color: var(--ink-white); line-height: 1;
  }
  .brand-rule {
    position: absolute; right: 60px; top: 130px;
    width: 420px; height: 1px; background: var(--ink-soft);
  }
  .contact {
    position: absolute; right: 60px; top: 160px;
    text-align: right;
  }
  .address { font-size: 22px; color: var(--ink-soft); letter-spacing: 0.5px; }
  .website { font-size: 20px; font-weight: 700; margin-top: 6px; }
  .line { display: flex; justify-content: flex-end; align-items: center; gap: 8px; margin-top: 8px; font-size: 20px; }
  .icon { width: 20px; height: 20px; flex: none; }
  .email { font-size: 19px; color: var(--ink-soft); }
  .person { position: absolute; right: 60px; text-align: right; }
  .person.broker { top: 330px; }
  .person.realtor { top: 455px; }
  .person-name { font-size: 38px; color: var(--ink-white); }
  .person-title { font-size: 20px; color: var(--ink-muted); margin-left: 10px; }
  .divider {
    position: absolute; right: 60px; top: 435px;
    width: 500px; height: 1px; background: var(--rule-purple);
  }
</style>
</head>
<body>
  <div class="card">
    <div class="emboss-mark" role="img" aria-label="Large embossed brand mark decoration"></div>

    <div class="brand">
      <div class="brand-dot"></div>
      <div class="brand-name">Halvern Properties</div>
    </div>
    <div class="brand-rule"></div>

    <div class="contact">
      <p class="address">518B W. Cottonwell Ave. Ferrow Glen, ZX. 70999</p>
      <p class="website">WWW.HALVERNPROPERTIES-EXAMPLE.COM</p>
      <p class="line">
        <svg class="icon" viewBox="0 0 20 20"><circle cx="10" cy="10" r="10" fill="#f4f2f6"/><path d="M6.5 5.5l2 0 1 2.6-1.3 1a6 6 0 0 0 2.7 2.7l1-1.3 2.6 1v2a1 1 0 0 1-1 1A8.5 8.5 0 0 1 5.5 6.5a1 1 0 0 1 1-1z" fill="#050407"/></svg>
        <span>(555).841.2600</span>
      </p>
      <p class="line email">
        <svg class="icon" viewBox="0 0 20 20"><circle cx="10" cy="10" r="10" fill="#f4f2f6"/><rect x="5" y="6.5" width="10" height="7" fill="#050407"/><path d="M5 6.5l5 4 5-4" stroke="#f4f2f6" stroke-width="1" fill="none"/></svg>
        <span>halvern@halvernproperties-example.com</span>
      </p>
    </div>

    <div class="person broker">
      <p><span class="person-name">Marla Halvern</span><span class="person-title">Broker</span></p>
      <p class="line">
        <svg class="icon" viewBox="0 0 20 20"><circle cx="10" cy="10" r="10" fill="#f4f2f6"/><rect x="7" y="4.5" width="6" height="11" rx="1" fill="#050407"/><rect x="8" y="6" width="4" height="7" fill="#f4f2f6"/></svg>
        <span>(555).316.4827</span>
      </p>
    </div>

    <div class="divider"></div>

    <div class="person realtor">
      <p><span class="person-name">Tessa Halvern</span><span class="person-title">Realtor</span></p>
      <p class="line">
        <svg class="icon" viewBox="0 0 20 20"><circle cx="10" cy="10" r="10" fill="#f4f2f6"/><rect x="7" y="4.5" width="6" height="11" rx="1" fill="#050407"/><rect x="8" y="6" width="4" height="7" fill="#f4f2f6"/></svg>
        <span>(555).627.9154</span>
      </p>
    </div>
  </div>
</body>
</html>
```